Menu Board that is editable in Plakly (NO AI).

I am looking for help creating a simple, highly readable menu system for **Wobble Buns**, a scratch-made bakery concept centered around large rolls that customers can order simply or customize.

The overall design should feel **playful, unexpected, slightly quirky, and full of personality without feeling juvenile, chaotic, or difficult to read**.

I want the menu to be fun and memorable, but the ordering system itself needs to be extremely easy to understand at a glance.

## Brand Personality

Wobble Buns balances two sides:

**Wobble** = playful, imperfect, unexpected, expressive, slightly weird, and willing to break the rules.

**Buns** = familiar, dependable, scratch-made, comforting, and approachable.

The food is taken seriously, but the brand should not take itself too seriously.

The menu should reflect that balance. I would like personality to come through in typography, graphic elements, shapes, illustrations, imperfect details, and subtle graffiti or hand-drawn influences rather than making the information itself chaotic.

## Typography

The two primary fonts will be:

**Oleo Ugly**
Used selectively for personality, large headlines, category names, featured words, or graphic accents.

**Montserrat**
Used for descriptions, prices, ingredients, instructions, and anything that needs to be read quickly.

Oleo Ugly should provide the playful, slightly unpredictable **Wobble** element, while Montserrat keeps the menu grounded, organized, and functional.

## Brand Color Palette

The Wobble Buns color palette is:

**Crimson Ink**
#8B162B

**Dusty Rose**
#F9B6B8

**Cosmic Latte**
#F6F3CF

**Neon Pear**
#C6B63B

**Burnt Sienna**
#F37521

**Arctic Blue**
#BAD2E8

These colors are intended to work as a flexible brand system rather than all being used equally on every piece.

For the **Ember Lineup**, I envision leaning primarily into:

* Crimson Ink
* Cosmic Latte
* Burnt Sienna
* Neon Pear

The overall Wobble Buns palette should remain recognizable, while seasonal menus can emphasize different combinations of colors.

I would like the colors to feel bold and slightly unexpected rather than traditionally rustic or “fall farmhouse.” The Ember menu can feel warm and seasonal without relying heavily on brown, muted orange, wood grain, or other conventional autumn design elements.

## Menu Structure

The ordering system has three primary categories:

### GO CLASSIC — $6

Customers choose:

* One roll
* One icing

### GO SIGNATURE — $7

Customers choose one of our pre-designed seasonal Signature Buns.

These are curated seasonal combinations created by us and will change throughout the year.

### GO WOBBLE — $7

Customers build their own roll by choosing:

* One roll
* One icing
* One filling
* One drizzle
* One crunch

The most important design goal is that a customer should be able to look at the menu and understand these three ordering options almost immediately.

## Pick Your Roll

The three Wobble Buns bases are:

### CLASSIC CINNAMON ROLL

Soft, fluffy and unapologetically classic, with our signature cinnamon filling.

### CARAMEL ROLL

Soft, buttery and caramel-forward with no cinnamon, so the other flavors get to shine.

### SOURDOUGH CINNAMON ROLL

Our classic cinnamon roll with the deeper flavor and character of sourdough.

These descriptions should be visible but secondary to the roll names. The customer should first see the three choices, then be able to quickly understand what makes each one different.

## Pick Your Icing

### CLASSIC BUTTERCREAM

The one that started it all. Rich, silky, buttery-sweet, and generously decadent.

### CREAM CHEESE ICING

The Marlowe Staple. Thick, creamy, tangy, and perfectly sweet with that unmistakable cream cheese finish.

### VANILLA SWEET CREAM ICING

Light, fluffy, and silky with a soft vanilla sweetness. Think whipped cream meets icing: airy, creamy, and made to melt right into your roll.

The icing names should remain easy to scan, with the descriptions present as supporting information rather than dominating the layout.

## Ember Lineup

The first seasonal menu will be the **Ember Lineup**, running September through November.

The available finishes will remain mostly consistent throughout the Ember season, while the featured Signature Buns can change monthly.

## September Signature Buns

### CARAMEL APPLE

Classic Cinnamon Roll
Cream Cheese Icing
Apple
Caramel
Shortbread Crumble

### BROWNIE SUNDAE

Caramel Roll
Vanilla Sweet Cream Icing
Chocolate Brownie
Chocolate Ganache
Salted Peanuts

### TALLWICK COOKIE CRUNCH

Sourdough Cinnamon Roll
Classic Buttercream
Tallwick Cookie Butter
Browned Butter Glaze
Tallwick Cookie Crumbles

The Signature Buns should be one of the most visually appealing parts of the menu. These are combinations we have already designed for the customer, so they should feel easy to order and tempting at a glance.

## Go Wobble Finish Categories

Customers choosing **Go Wobble** select one option from each finishing category.

### ICING

* Classic Buttercream
* Cream Cheese Icing
* Vanilla Sweet Cream Icing

### FILLING

* Apple
* Pumpkin
* Chocolate Brownie
* Coconut Pecan
* Tallwick Cookie Butter

### DRIZZLE

* Classic Butter Glaze
* Browned Butter Glaze
* Caramel
* Espresso Glaze
* Coconut Glaze
* Chocolate Ganache

### CRUNCH

* Shortbread Crumble
* Salted Peanuts
* Chocolate Espresso Beans
* Tallwick Cookie Crumbles
* Toasted Coconut
* Candied Pecans
* Graham Cracker Crumbs

The four finishing categories should be visually distinct and easy to follow in order:

**Icing → Filling → Drizzle → Crunch**

The customer should immediately understand that they choose **one from each category**.

## Physical Menu Format

Space is limited and the menu will be suspended from the ceiling behind the counter.

The individual menu pieces will be approximately **8.5 × 11 landscape**, mounted to a lightweight rigid backing and hung as coordinated signs.

I currently envision approximately three menu boards:

### Board 1 — How Do You Roll?

A simple introduction to the three ways to order:

**Go Classic — $6**
Roll + Icing

**Go Signature — $7**
Choose one of our seasonal Signature Buns

**Go Wobble — $7**
Roll + Icing + Filling + Drizzle + Crunch

This board should be extremely simple and readable from a distance.

### Board 2 — Go Classic + September Signatures

One portion of the board should show the three roll choices and three icing choices, including their short descriptions.

The other portion should feature the current September Signature Buns.

### Board 3 — Go Wobble

This board should show:

**Pick Your Roll**

followed by four clearly organized finishing categories:

**Icing | Filling | Drizzle | Crunch**

This board contains the most information and should therefore have the strongest visual organization and the least unnecessary decoration.

## Design Direction

I would like the finished menu to feel:

* Playful
* Slightly unconventional
* Modern with handmade personality
* Bold
* Fun
* Friendly
* Approachable
* Easy to scan quickly
* Organized
* Adult and intentional rather than childish

I am interested in selective influences from **graffiti, hand-drawn graphics, paint marks, arrows, stars, doodles, imperfect lines, unexpected shapes, and layered typography**.

However, these elements should support the menu rather than interfere with readability.

I do not want the design to feel like a children's menu, overly rustic, overly polished or corporate, or visually chaotic.

Because the menu will hang overhead and customers will often read it from several feet away, **clarity and hierarchy are more important than fitting in extra decoration**.

The overall philosophy for the design is:

**The branding gets to misbehave.
The information does not.**

A customer should quickly understand:

**Go Classic** = keep it simple.
**Go Signature** = choose one of ours.
**Go Wobble** = build your own.

The final result should feel distinctive enough that someone immediately recognizes Wobble Buns has personality, while being simple enough that ordering requires almost no explanation from staff.

Target Market(s)

People who enjoy treats

Industry/Entity Type

Bakery

Requirements
Must have
• Simplicity to understand
Should not have
• No AI, No stock photos.

```html
<!DOCTYPE html>
<html lang="en">
<head>
<meta charset="utf-8">
<title>Wobble Buns – How Do You Roll?</title>
<link rel="stylesheet" href="https://fonts.googleapis.com/css2?family=Anton&family=Montserrat:wght@300;500;600&family=Rubik+Doodle+Shadow&display=swap">
<style>
  :root {
    --crimson-ink: #8B162B;
    --cosmic-latte: #F6F3CF;
    --paper: #FBF4E2;
    --neon-pear: #C6B63B;
    --burnt-sienna: #F37521;
    --sun-beige: #E9D39A;
    --ink: #111111;
    --rule: #6d6a63;
  }
  * { box-sizing: border-box; margin: 0; padding: 0; }
  html, body { width: 865px; height: 1200px; overflow: hidden; background: var(--ink); }
  .board {
    position: relative;
    width: 865px; height: 1200px;
    background: var(--ink);
    padding: 48px 46px;
  }
  .board__sheet {
    position: relative;
    width: 100%; height: 100%;
    background: var(--paper);
    overflow: hidden;
  }
  .paint-band, .crimson-moon, .sun-burst, .pear-swipe { position: absolute; display: block; }
  .paint-band { left: 0; top: 0; width: 700px; height: 330px; }
  .crimson-moon { right: -70px; top: -90px; width: 250px; height: 250px; border-radius: 50%; background: var(--crimson-ink); }
  .sun-burst { left: 418px; top: 78px; width: 160px; height: 160px; border-radius: 50%; background: var(--sun-beige); }
  .pear-swipe { left: 80px; top: 434px; width: 510px; height: 26px; }

  .title {
    position: absolute; left: 82px; top: 40px;
    font-family: "Rubik Doodle Shadow", system-ui, sans-serif;
    font-weight: 400; color: var(--ink);
    font-size: 118px; line-height: 0.98; letter-spacing: 2px;
  }
  .title span { display: block; }
  .title .title__second { margin-left: 10px; }

  .tagline {
    position: absolute; left: 183px; top: 356px;
    font-family: "Montserrat", sans-serif; font-weight: 300;
    font-size: 46px; line-height: 1.0; color: var(--ink); text-transform: uppercase;
  }

  .options { position: absolute; left: 56px; top: 484px; width: 660px; }
  .option {
    position: relative; display: flex; align-items: center;
    height: 190px; border-bottom: 2px solid var(--rule);
  }
  .option:first-child { height: 148px; }
  .option__badge {
    flex: none; width: 102px; height: 102px; border-radius: 50%;
    display: flex; align-items: center; justify-content: center;
    margin-left: 32px; margin-right: 44px;
    font-family: "Anton", sans-serif; font-size: 40px; color: var(--cosmic-latte);
  }
  .option--classic .option__badge { background: var(--crimson-ink); }
  .option--signature .option__badge { background: var(--burnt-sienna); }
  .option--wobble .option__badge { background: var(--neon-pear); }
  .option__text { width: 280px; }
  .option__name { font-family: "Anton", sans-serif; font-size: 78px; line-height: 1; color: var(--ink); letter-spacing: 1px; }
  .option__desc { font-family: "Montserrat", sans-serif; font-weight: 500; font-size: 17px; line-height: 1.2; color: var(--ink); margin-top: 10px; text-transform: uppercase; }
  .option__price {
    position: absolute; left: 582px; top: 50%; transform: translateY(-50%);
    border-left: 2px solid var(--rule); height: 104px;
    padding-left: 30px; display: flex; align-items: center;
    font-family: "Anton", sans-serif; font-size: 72px; line-height: 1;
  }
  .option__price sup { font-family: "Montserrat", sans-serif; font-weight: 600; font-size: 26px; color: var(--ink); align-self: flex-start; margin-top: 8px; margin-right: 4px; }
  .option--classic .option__price { color: var(--crimson-ink); }
  .option--signature .option__price { color: var(--burnt-sienna); }
  .option--wobble .option__price { color: var(--neon-pear); }

  .footer-band {
    position: absolute; left: 0; right: 0; bottom: 0; height: 88px;
    background: var(--crimson-ink);
    display: flex; align-items: center; justify-content: center;
    font-family: "Montserrat", sans-serif; font-weight: 500; font-size: 22px;
    color: var(--cosmic-latte); letter-spacing: 0.5px;
  }
</style>
</head>
<body>
<main class="board">
  <div class="board__sheet">
    <svg class="paint-band" viewBox="0 0 700 330" role="img" aria-label="Orange paint brush strokes behind the headline">
      <path d="M0 10 L560 0 L610 60 L700 70 L690 170 L640 230 L470 250 L330 300 L120 320 L0 330 Z" fill="var(--burnt-sienna)"/>
    </svg>
    <span class="crimson-moon" role="img" aria-label="Crimson circle accent"></span>
    <span class="sun-burst" role="img" aria-label="Pale sunburst shape"></span>

    <h1 class="title"><span>Wobble</span><span class="title__second">Buns</span></h1>

    <svg class="pear-swipe" viewBox="0 0 510 26" role="img" aria-label="Neon pear paint swipe">
      <path d="M0 14 Q250 0 510 4 L505 18 Q250 16 4 26 Z" fill="var(--neon-pear)"/>
    </svg>
    <p class="tagline">How do<br>you roll ?</p>

    <section class="options">
      <article class="option option--classic">
        <div class="option__badge">GO</div>
        <div class="option__text">
          <h2 class="option__name">CLASSIC</h2>
          <p class="option__desc">Roll + Icing</p>
        </div>
        <div class="option__price"><sup>$</sup>6</div>
      </article>
      <article class="option option--signature">
        <div class="option__badge">GO</div>
        <div class="option__text">
          <h2 class="option__name">SIGNATURE</h2>
          <p class="option__desc">Choose one of our<br>seasonal signature buns</p>
        </div>
        <div class="option__price"><sup>$</sup>7</div>
      </article>
      <article class="option option--wobble">
        <div class="option__badge">GO</div>
        <div class="option__text">
          <h2 class="option__name">WOBBLE</h2>
          <p class="option__desc">Roll + Icing + Filling +<br>Drizzle + Crunch</p>
        </div>
        <div class="option__price"><sup>$</sup>7</div>
      </article>
    </section>

    <footer class="footer-band">SCRATCH-MADE. BOLD FLAVOR. ZERO BRORING.</footer>
  </div>
</main>
</body>
</html>
```